1/4 page magazine ad

We would like a 1/4 ad in a magazine advertising a doctor in our practice. Dr. Clara Mendt, DC is the only Female Brinley Certified chiropractor in Williamsburg, VA. We would like the ad to include a large eye catching picture of a woman's pregnant belly, as the Brinley technique is for pregnant women. Please take a look at our previous ad that we have had done to see some of the elements that we liked in our other ad.

```html
<!DOCTYPE html>
<html lang="en">
<head>
<meta charset="utf-8">
<title>Harbor Spine Center – Quarter Page Ad</title>
<link rel="stylesheet" href="https://fonts.googleapis.com/css2?family=Bebas+Neue&family=Poppins:wght@400;500;600;700;800&display=swap">
<style>
  :root {
    --maroon: #8b0e10;
    --maroon-dark: #6f0a0c;
    --charcoal: #2b2b2b;
    --gold: #fbbd16;
    --page-bg: #c6c6c6;
    --ink: #2a2a2a;
    --white: #ffffff;
    --review-blue: #4a86e8;
  }
  * { box-sizing: border-box; margin: 0; padding: 0; }
  html, body {
    width: 890px; height: 1200px; overflow: hidden;
    background: var(--page-bg);
    font-family: "Poppins", Arial, sans-serif;
  }
  .ad {
    position: absolute; left: 30px; top: 335px;
    width: 830px; height: 530px; overflow: hidden;
    background:
      radial-gradient(circle at 60px 40px, rgba(255,255,255,.9) 0 40px, transparent 60px),
      radial-gradient(circle at 300px 330px, rgba(255,255,255,.8) 0 50px, transparent 90px),
      radial-gradient(circle at 480px 60px, rgba(255,255,255,.8) 0 30px, transparent 60px),
      linear-gradient(180deg, #f4f4f4, #e9e9e9 60%, #f6f6f6);
    box-shadow: 6px 8px 14px rgba(0,0,0,.35);
  }
  .ad > * { position: absolute; }

  .hero-photo {
    left: 530px; top: 0; width: 300px; height: 470px;
    background: linear-gradient(160deg, #3a3a3a 0%, #8e8e8e 30%, #b4b4b4 55%, #7a7a7a 80%, #5a5a5a 100%);
  }

  .headline {
    left: 38px; top: 26px; display: flex; align-items: center; gap: 12px;
    font-family: "Bebas Neue", Impact, sans-serif; font-size: 80px; line-height: 1;
    color: var(--maroon); letter-spacing: -0.5px;
  }
  .headline .or {
    width: 44px; height: 44px; border-radius: 50%;
    background: var(--gold); color: var(--maroon-dark);
    font-family: "Poppins", Arial, sans-serif; font-weight: 700; font-size: 18px;
    display: flex; align-items: center; justify-content: center;
  }

  .services-band {
    left: 0; top: 109px; width: 519px; height: 41px;
    background: var(--charcoal); border-radius: 0 10px 10px 0;
    display: flex; align-items: center; padding-left: 40px; gap: 30px;
    color: var(--white); font-weight: 700; font-size: 28px; letter-spacing: .3px;
  }
  .services-band span { display: flex; align-items: center; gap: 6px; }
  .services-band svg { width: 22px; height: 22px; }

  .treating-tab {
    left: 0; top: 150px; width: 206px; height: 39px;
    background: var(--maroon);
    clip-path: polygon(0 0, 100% 0, 86% 100%, 0 100%);
    color: var(--white); font-weight: 700; font-size: 20px; letter-spacing: 4.5px;
    display: flex; align-items: center; padding-left: 42px;
  }

  .condition-list { list-style: none; top: 206px; }
  .condition-list li {
    height: 36px; display: flex; align-items: center; gap: 9px;
    font-weight: 600; font-size: 19px; color: var(--ink);
  }
  .condition-list svg { width: 22px; height: 22px; fill: var(--maroon); }
  .condition-list.col-a { left: 42px; }
  .condition-list.col-b { left: 222px; }
  .list-divider { left: 202px; top: 210px; width: 1px; height: 100px; background: #cfcfcf; }

  .insurance-seal { left: 372px; top: 168px; width: 156px; height: 156px; }
  .insurance-seal .petal {
    position: absolute; inset: 12px; background: var(--maroon); border-radius: 22%;
  }
  .insurance-seal .petal:nth-child(2) { transform: rotate(30deg); }
  .insurance-seal .petal:nth-child(3) { transform: rotate(60deg); }
  .seal-text {
    position: absolute; inset: 0; display: flex; flex-direction: column;
    align-items: center; justify-content: center; text-align: center;
    font-size: 16.5px; line-height: 1.15; color: var(--white); font-weight: 500;
  }
  .seal-text strong { color: var(--gold); font-weight: 700; }

  .doctor-photo {
    left: 34px; top: 323px; width: 104px; height: 104px; border-radius: 50%;
    border: 4px solid var(--gold); z-index: 3;
    background: radial-gradient(circle at 50% 40%, #c9a48c 0 22%, #5c3b2a 40%, #3f5a3a 75%);
  }
  .name-band {
    left: 112px; top: 336px; width: 242px; height: 34px;
    background: var(--maroon);
    clip-path: polygon(0 0, 88% 0, 100% 100%, 0 100%);
    color: var(--white); font-weight: 700; font-size: 17px;
    display: flex; align-items: center; padding-left: 40px; letter-spacing: .3px;
  }
  .contact-band {
    left: 112px; top: 370px; width: 444px; height: 56px; background: var(--gold);
    display: flex; align-items: center; padding-left: 38px; z-index: 2;
  }
  .contact-band .phone {
    display: flex; align-items: center; gap: 5px;
    color: var(--maroon); font-weight: 700; font-size: 21px; letter-spacing: .5px;
    padding-right: 12px; border-right: 1px solid rgba(139,14,16,.35); height: 26px;
  }
  .contact-band .phone svg { width: 17px; height: 17px; }
  .contact-band .address {
    display: flex; gap: 4px; padding-left: 12px;
    font-size: 11.5px; line-height: 1.25; color: var(--ink); font-weight: 500;
  }
  .contact-band .address svg { width: 10px; height: 13px; flex: none; margin-top: 1px; }

  .rating { left: 366px; top: 340px; display: flex; align-items: center; gap: 7px; }
  .rating .dot { width: 20px; height: 20px; border-radius: 50%; background: var(--review-blue); }
  .rating .score { font-weight: 600; font-size: 19px; color: var(--ink); }
  .rating .stars { color: var(--gold); font-size: 14px; letter-spacing: 1px; }

  .practice-name { left: 38px; top: 465px; display: flex; align-items: center; gap: 8px; }
  .practice-name .mark { width: 22px; height: 22px; background: var(--maroon); }
  .practice-name span { color: var(--maroon); font-weight: 700; font-size: 14px; }

  .badge { top: 455px; width: 44px; height: 44px; }
  .badge.award { left: 248px; background: var(--charcoal); border-radius: 50%; border: 3px solid var(--gold); }
  .badge.listing { left: 304px; background: #3c78b5; border-radius: 3px; border-top: 6px solid #e05a2b; }

  .tech-note { left: 372px; top: 457px; }
  .tech-note h3 {
    color: var(--maroon); font-weight: 700; font-size: 12.5px; line-height: 1.05; letter-spacing: .2px;
  }
  .tech-note p { font-size: 10.5px; color: var(--ink); margin-top: 6px; }

  .web-band {
    left: 559px; top: 466px; width: 271px; height: 32px;
    background: var(--charcoal); border-radius: 8px 0 0 8px;
    color: var(--white); font-size: 11px; letter-spacing: .3px;
    display: flex; align-items: center; padding-left: 14px;
  }
  .web-band b { font-weight: 700; }
</style>
</head>
<body>
  <article class="ad">
    <div class="hero-photo" role="img" aria-label="Black and white photo of a pregnant woman holding her belly"></div>

    <h1 class="headline"><span>NECK</span><span class="or">OR</span><span>BACK PAIN?</span></h1>

    <div class="services-band">
      <span><svg viewBox="0 0 24 24" fill="#fbbd16"><circle cx="7" cy="6" r="2.5"/><rect x="3" y="14" width="18" height="3" rx="1"/><path d="M5 13l4-4 6 2 3-3 1 2-4 4-6-2-2 1z"/></svg>CHIROPRACTIC</span>
      <span><svg viewBox="0 0 24 24" fill="#fbbd16"><path d="M4 22l3-14 3 1-1 13zM10 22l2-15 3 1v14zM16 22l1-12 3 1-1 11z"/></svg>MASSAGE</span>
    </div>

    <div class="treating-tab">TREATING</div>

    <ul class="condition-list col-a">
      <li><svg viewBox="0 0 24 24"><circle cx="18" cy="5" r="3"/><path d="M6 12l9-4 2 3-5 3-1 8H8l1-7-3 1z"/></svg>Back Pain</li>
      <li><svg viewBox="0 0 24 24"><path d="M12 2a8 8 0 0 1 8 8l-2 3v4h-4v5H6v-6a8 8 0 0 1 6-14z"/></svg>Neck Pain</li>
      <li><svg viewBox="0 0 24 24"><circle cx="12" cy="9" r="5"/><path d="M4 22v-4l4-3h8l4 3v4zM3 5l3 2M21 5l-3 2"/></svg>Headaches</li>
    </ul>
    <div class="list-divider"></div>
    <ul class="condition-list col-b">
      <li><svg viewBox="0 0 24 24"><path d="M6 3h9v4h-3v15H9V7H6z"/><circle cx="18" cy="4" r="2"/></svg>Joint Pain</li>
      <li><svg viewBox="0 0 24 24"><path d="M6 2h6l2 8h4v4h-6l-1 8H7l1-10z"/></svg>Sciatica</li>
      <li><svg viewBox="0 0 24 24"><circle cx="13" cy="5" r="3"/><path d="M10 9h5l-2 8-3 5H8l2-6z"/></svg>Fatigue</li>
    </ul>

    <div class="insurance-seal">
      <div class="petal"></div><div class="petal"></div><div class="petal"></div>
      <div class="seal-text">MEDICARE<br>&amp; MOST<strong>INSURANCE<br>ACCEPTED</strong></div>
    </div>

    <div class="doctor-photo" role="img" aria-label="Portrait photo of Dr. Clara Mendt"></div>
    <div class="name-band">DR. CLARA MENDT</div>
    <div class="rating" aria-label="Reviews 5.0 out of 5"><span class="dot"></span><span class="score">5.0</span><span class="stars">★★★★★</span></div>
    <div class="contact-band">
      <div class="phone"><svg viewBox="0 0 24 24"><circle cx="12" cy="12" r="11" fill="#8b0e10"/><path d="M8 6l2 0 1 3-1.5 1a7 7 0 0 0 4 4l1-1.5 3 1v2a2 2 0 0 1-2 2A10 10 0 0 1 6 8a2 2 0 0 1 2-2z" fill="#fbbd16"/></svg>757-555-0148</div>
      <div class="address"><svg viewBox="0 0 10 14"><path d="M5 0a5 5 0 0 1 5 5c0 4-5 9-5 9S0 9 0 5a5 5 0 0 1 5-5z" fill="#8b0e10"/><circle cx="5" cy="5" r="2" fill="#fbbd16"/></svg><span>2215 Linden Row, # 104,<br>Williamsburg, VA 23185</span></div>
    </div>

    <div class="practice-name"><span class="mark"></span><span>Harbor Spine Center</span></div>
    <div class="badge award" aria-label="Readers' choice award badge"></div>
    <div class="badge listing" aria-label="Best-of listing badge"></div>

    <div class="tech-note">
      <h3>ADVANCE CHIROPRACTIC<br>TECHNOLOGY</h3>
      <p>Our Goal is getting you pain free</p>
    </div>

    <div class="web-band">www.<b>harborspinecenter</b>.com</div>
  </article>
</body>
</html>
```